SOCIAL MEDIA BANNERS FOR MIRVO KALT , ONLINT TOUR BOOKING PLATFORM

We need attractive, creative, and professionally designed social media banners for Mirvo Kalt, an innovative online tour booking company.

Banner Requirements:

Platforms: Facebook, Instagram, YouTube, LinkedIn, Pinterest, Twitter (X), and TikTok.

Visuals: Include eye-catching imagery highlighting popular tourist attractions (e.g., Niagara Falls, famous Ontario sites, and global landmarks).

Design Style:

Clearly feature "Mirvo Kalt" prominently in large, bold, white letters.

Incorporate subtle animations or illustrations of bees flying around or inside the letters to reinforce our brand identity.

Slogan: Integrate our slogan creatively: "Going Bee-yond! 🐝"

Colors: Emphasize our brand colors; ensure high contrast for readability.

Consistency: Each banner design should share a common visual theme yet be optimized for each platform’s specific dimensions and layout guidelines.

File Formats: Provide high-resolution banners in JPEG/PNG and source files (PSD, AI, or similar editable format).

Preferred approach:

Present multiple design concepts initially, allowing us to select the most suitable creative direction.

Upon approval, logos and brand guidelines will be shared to assist in the design process.

Target Market(s)

Tourists and travelers primarily in Canada, with an intention to expand globally. Audience typically ranges from young adults to mature travelers seeking unique and memorable tour experiences.

Industry/Entity Type

Tourism , Travel

Colors

Designer to choose colors to be used in the design.

Requirements
Must have
• there is no must its depends how its looks ,
Nice to have
• Clearly visible branding: "Mirvo Kalt" prominently displayed. Visual representation of bees flying around or through the letters. Images or illustrations depicting popular tour attractions.

```html
<!DOCTYPE html>
<html lang="en">
<head>
<meta charset="UTF-8">
<title>Mirvo Kalt — Social Banners</title>
<link rel="stylesheet" href="https://fonts.googleapis.com/css2?family=Poppins:wght@400;500;600;700&family=Allura&display=swap">
<style>
  :root{
    --stage:#d6d6d6;
    --royal:#0d2aa0;
    --royal-deep:#0a2287;
    --navy:#141a4d;
    --navy-band:#1c2466;
    --honey:#fcb813;
    --white:#ffffff;
    --sans:'Poppins', Arial, sans-serif;
    --script:'Allura', cursive;
  }
  *{margin:0;padding:0;box-sizing:border-box}
  html,body{width:1200px;height:1200px;overflow:hidden}
  body{background:var(--stage);position:relative;font-family:var(--sans);color:var(--white)}
  .banner{position:absolute;overflow:hidden;background:linear-gradient(180deg,var(--royal) 0%,var(--royal-deep) 60%,#0b249a 100%)}
  .banner--portrait{left:132px;top:106px;width:453px;height:566px}
  .banner--square{left:609px;top:220px;width:453px;height:453px}
  .banner--wide{left:132px;top:694px;width:746px;height:392px}
  .abs{position:absolute}
  .side-strip{position:absolute;top:0;background:var(--navy);opacity:.85}
  .skyline{position:absolute;background:radial-gradient(ellipse at 50% 80%,rgba(80,110,210,.3),rgba(13,42,160,0) 70%)}
  .brand{position:absolute;display:flex;align-items:center;gap:6px;white-space:nowrap;transform:translateX(-50%)}
  .brand__name{font-weight:600;color:var(--white);letter-spacing:.5px;line-height:1}
  .brand__dot{border-radius:50%;background:var(--honey);flex:none}
  .tagline{position:absolute;color:var(--honey);font-weight:500;letter-spacing:1px;white-space:nowrap;transform:translateX(-50%);line-height:1}
  .intro{position:absolute;font-weight:400;letter-spacing:.6px;line-height:1.45}
  .intro b{font-weight:700}
  .script{position:absolute;font-family:var(--script);color:var(--white);line-height:1}
  .beeyond{position:absolute;color:var(--honey);font-weight:600;white-space:nowrap;line-height:1}
  .hex{position:absolute}
  .bee{position:absolute;border-radius:8px;background:linear-gradient(160deg,rgba(110,130,210,.55) 0%,rgba(60,60,80,.6) 55%,rgba(230,180,40,.6) 100%)}
  .dots{position:absolute}
  .footer{position:absolute;left:0;bottom:0;display:flex;align-items:center}
  .footer__phone{display:flex;align-items:center;font-weight:700;white-space:nowrap}
  .footer__contact{display:flex;align-items:center;gap:6px;font-weight:500;letter-spacing:.4px;white-space:nowrap}
  .icon-phone{border-radius:50%;background:#e9e9ef;display:flex;align-items:center;justify-content:center;flex:none}
  .hex-label{font-family:var(--sans);font-weight:700;fill:var(--white)}
</style>
</head>
<body>

<svg width="0" height="0" style="position:absolute" aria-hidden="true">
  <defs>
    <linearGradient id="photo-falls" x1="0" y1="0" x2="1" y2="1">
      <stop offset="0" stop-color="#c9622c"/><stop offset=".35" stop-color="#6d8c5a"/>
      <stop offset=".6" stop-color="#7fc6e0"/><stop offset="1" stop-color="#3d5a3c"/>
    </linearGradient>
    <linearGradient id="photo-castle" x1="0" y1="0" x2="0" y2="1">
      <stop offset="0" stop-color="#5f9de0"/><stop offset=".45" stop-color="#9a958c"/>
      <stop offset=".75" stop-color="#6d7c55"/><stop offset="1" stop-color="#4c5a3f"/>
    </linearGradient>
    <linearGradient id="photo-wall" x1="0" y1="0" x2="0" y2="1">
      <stop offset="0" stop-color="#efd9c4"/><stop offset=".35" stop-color="#5f8d4e"/>
      <stop offset=".7" stop-color="#a7764f"/><stop offset="1" stop-color="#8a8a86"/>
    </linearGradient>
    <pattern id="dot-grid" width="12" height="12" patternUnits="userSpaceOnUse">
      <circle cx="3" cy="3" r="2.2" fill="#ffffff"/>
    </pattern>
  </defs>
</svg>

<!-- Portrait banner -->
<section class="banner banner--portrait">
  <div class="side-strip" style="left:0;width:43px;height:517px"></div>
  <div class="side-strip" style="left:410px;width:44px;height:517px"></div>
  <div class="skyline" role="img" aria-label="Faint collage of world landmarks" style="left:0;top:120px;width:453px;height:400px"></div>

  <div class="bee" role="img" aria-label="Small bee flying with a dashed flight trail" style="left:103px;top:11px;width:30px;height:38px"></div>
  <div class="brand" style="left:226px;top:62px"><span class="brand__dot" style="width:14px;height:14px"></span><span class="brand__name" style="font-size:36px">Mirvo Kalt</span></div>
  <div class="tagline" style="left:226px;top:98px;font-size:15px">Going Bee-yond!</div>

  <p class="intro" style="left:56px;top:148px;width:175px;font-size:10.5px">Let the bees lead the way! Discover breathtaking desti-nations with <b>Mirvo Kalt</b>, your passport to unforgettable journeys.</p>

  <div class="bee" role="img" aria-label="Large bee in flight with a looping dashed trail" style="left:362px;top:111px;width:62px;height:87px"></div>

  <svg class="hex" style="left:207px;top:164px" width="183" height="159" viewBox="0 0 200 174">
    <polygon points="50,2 150,2 198,87 150,172 50,172 2,87" fill="var(--honey)"/>
    <polygon role="img" aria-label="Photo of Niagara Falls" points="58,12 142,12 186,87 142,162 58,162 14,87" fill="url(#photo-falls)"/>
    <polygon points="33,118 167,118 144,158 56,158" fill="var(--navy-band)" opacity=".9"/>
    <text class="hex-label" x="100" y="136" text-anchor="middle" font-size="15">NIAGARA</text>
    <text class="hex-label" x="100" y="153" text-anchor="middle" font-size="15">FALLS</text>
  </svg>
  <svg class="hex" style="left:56px;top:250px" width="183" height="159" viewBox="0 0 200 174">
    <polygon points="50,2 150,2 198,87 150,172 50,172 2,87" fill="var(--honey)"/>
    <polygon role="img" aria-label="Photo of a historic Ontario castle" points="58,12 142,12 186,87 142,162 58,162 14,87" fill="url(#photo-castle)"/>
    <polygon points="33,118 167,118 144,158 56,158" fill="var(--navy-band)" opacity=".9"/>
    <text class="hex-label" x="100" y="136" text-anchor="middle" font-size="15">ONTARIO</text>
    <text class="hex-label" x="100" y="153" text-anchor="middle" font-size="15">SITES</text>
  </svg>
  <svg class="hex" style="left:207px;top:336px" width="183" height="159" viewBox="0 0 200 174">
    <polygon points="50,2 150,2 198,87 150,172 50,172 2,87" fill="var(--honey)"/>
    <polygon role="img" aria-label="Photo of a great ancient wall over hills" points="58,12 142,12 186,87 142,162 58,162 14,87" fill="url(#photo-wall)"/>
    <polygon points="33,118 167,118 144,158 56,158" fill="var(--navy-band)" opacity=".9"/>
    <text class="hex-label" x="100" y="136" text-anchor="middle" font-size="15">GLOBAL</text>
    <text class="hex-label" x="100" y="153" text-anchor="middle" font-size="15">LANDMARKS</text>
  </svg>

  <div class="script" style="left:40px;top:416px;font-size:66px">Going</div>
  <div class="beeyond" style="left:137px;top:481px;font-size:16px">Bee-yond!</div>
  <svg class="dots" style="left:420px;top:468px" width="24" height="60"><rect width="24" height="60" fill="url(#dot-grid)"/></svg>

  <div class="footer" style="right:0;height:49px;padding-left:21px;gap:12px">
    <div class="footer__phone" style="gap:6px;font-size:19px">
      <span class="icon-phone" style="width:22px;height:22px"><svg width="12" height="12" viewBox="0 0 24 24"><path d="M6.6 10.8a15 15 0 0 0 6.6 6.6l2.2-2.2c.3-.3.7-.4 1-.2 1.1.4 2.3.6 3.6.6.6 0 1 .4 1 1V20c0 .6-.4 1-1 1A17 17 0 0 1 3 4c0-.6.4-1 1-1h3.5c.6 0 1 .4 1 1 0 1.3.2 2.5.6 3.6.1.3 0 .7-.2 1z" fill="var(--navy)"/></svg></span>0147 258 369</div>
    <div class="footer__contact" style="font-size:10.5px">
      <svg width="11" height="9" viewBox="0 0 22 16"><rect x="1" y="1" width="20" height="14" fill="none" stroke="#fff" stroke-width="2"/><path d="M1 1l10 8 10-8" fill="none" stroke="#fff" stroke-width="2"/></svg>
      info@mirvokalt.com &nbsp;|&nbsp; www.Mirvokalt.com</div>
  </div>
</section>

<!-- Square banner -->
<section class="banner banner--square">
  <div class="side-strip" style="left:0;width:61px;height:416px"></div>
  <div class="side-strip" style="left:392px;width:61px;height:416px"></div>
  <div class="skyline" role="img" aria-label="Faint collage of world landmarks" style="left:0;top:80px;width:453px;height:340px"></div>

  <div class="bee" role="img" aria-label="Small bee flying with a dashed flight trail" style="left:106px;top:10px;width:27px;height:31px"></div>
  <div class="brand" style="left:226px;top:47px"><span class="brand__dot" style="width:12px;height:12px"></span><span class="brand__name" style="font-size:32px">Mirvo Kalt</span></div>
  <div class="tagline" style="left:226px;top:82px;font-size:13.5px">Going Bee-yond!</div>

  <p class="intro" style="left:80px;top:113px;width:150px;font-size:8.6px;line-height:1.3">Let the bees lead the way! Discover breathtaking desti-nations with <b>Mirvo Kalt</b>, your passport to unforgettable journeys.</p>

  <div class="bee" role="img" aria-label="Large bee in flight with a looping dashed trail" style="left:353px;top:44px;width:63px;height:84px"></div>
  <svg class="dots" style="left:425px;top:12px" width="24" height="60"><rect width="24" height="60" fill="url(#dot-grid)"/></svg>

  <svg class="hex" style="left:210px;top:108px" width="168" height="146" viewBox="0 0 200 174">
    <polygon points="50,2 150,2 198,87 150,172 50,172 2,87" fill="var(--honey)"/>
    <polygon role="img" aria-label="Photo of Niagara Falls" points="58,12 142,12 186,87 142,162 58,162 14,87" fill="url(#photo-falls)"/>
    <polygon points="33,118 167,118 144,158 56,158" fill="var(--navy-band)" opacity=".9"/>
    <text class="hex-label" x="100" y="136" text-anchor="middle" font-size="15">NIAGARA</text>
    <text class="hex-label" x="100" y="153" text-anchor="middle" font-size="15">FALLS</text>
  </svg>
  <svg class="hex" style="left:74px;top:182px" width="168" height="146" viewBox="0 0 200 174">
    <polygon points="50,2 150,2 198,87 150,172 50,172 2,87" fill="var(--honey)"/>
    <polygon role="img" aria-label="Photo of a historic Ontario castle" points="58,12 142,12 186,87 142,162 58,162 14,87" fill="url(#photo-castle)"/>
    <polygon points="33,118 167,118 144,158 56,158" fill="var(--navy-band)" opacity=".9"/>
    <text class="hex-label" x="100" y="136" text-anchor="middle" font-size="15">ONTARIO</text>
    <text class="hex-label" x="100" y="153" text-anchor="middle" font-size="15">SITES</text>
  </svg>
  <svg class="hex" style="left:211px;top:263px" width="168" height="146" viewBox="0 0 200 174">
    <polygon points="50,2 150,2 198,87 150,172 50,172 2,87" fill="var(--honey)"/>
    <polygon role="img" aria-label="Photo of a great ancient wall over hills" points="58,12 142,12 186,87 142,162 58,162 14,87" fill="url(#photo-wall)"/>
    <polygon points="33,118 167,118 144,158 56,158" fill="var(--navy-band)" opacity=".9"/>
    <text class="hex-label" x="100" y="136" text-anchor="middle" font-size="15">GLOBAL</text>
    <text class="hex-label" x="100" y="153" text-anchor="middle" font-size="15">LANDMARKS</text>
  </svg>

  <div class="script" style="left:57px;top:326px;font-size:56px">Going</div>
  <div class="beeyond" style="left:142px;top:383px;font-size:15px">Bee-yond!</div>

  <div class="footer" style="right:0;height:37px;padding-left:25px;gap:24px;background:var(--royal-deep)">
    <div class="footer__phone" style="gap:5px;font-size:16px">
      <span class="icon-phone" style="width:18px;height:18px"><svg width="10" height="10" viewBox="0 0 24 24"><path d="M6.6 10.8a15 15 0 0 0 6.6 6.6l2.2-2.2c.3-.3.7-.4 1-.2 1.1.4 2.3.6 3.6.6.6 0 1 .4 1 1V20c0 .6-.4 1-1 1A17 17 0 0 1 3 4c0-.6.4-1 1-1h3.5c.6 0 1 .4 1 1 0 1.3.2 2.5.6 3.6.1.3 0 .7-.2 1z" fill="var(--navy)"/></svg></span>0147 258 369</div>
    <div class="footer__contact" style="font-size:10.5px">
      <svg width="11" height="9" viewBox="0 0 22 16"><rect x="1" y="1" width="20" height="14" fill="none" stroke="#fff" stroke-width="2"/><path d="M1 1l10 8 10-8" fill="none" stroke="#fff" stroke-width="2"/></svg>
      info@mirvokalt.com &nbsp;|&nbsp; www.Mirvokalt.com</div>
  </div>
</section>

<!-- Wide banner -->
<section class="banner banner--wide">
  <div class="side-strip" style="left:0;top:0;width:334px;height:47px"></div>
  <div class="skyline" role="img" aria-label="Faint collage of world landmarks" style="left:200px;top:0;width:546px;height:392px"></div>
  <svg class="abs" style="left:0;top:0" width="746" height="130" role="img" aria-label="Golden panel with a pagoda photo">
    <polygon points="334,0 523,0 552,45 508,113 384,119" fill="var(--honey)" opacity=".92"/>
  </svg>

  <div class="bee" role="img" aria-label="Small bee flying with a dashed flight trail" style="left:62px;top:14px;width:36px;height:47px"></div>
  <div class="brand" style="left:179px;top:91px"><span class="brand__dot" style="width:13px;height:13px"></span><span class="brand__name" style="font-size:33px">Mirvo Kalt</span></div>
  <div class="tagline" style="left:179px;top:128px;font-size:14px">Going Bee-yond!</div>

  <div class="script" style="left:32px;top:138px;font-size:88px">Going</div>
  <div class="beeyond" style="left:174px;top:226px;font-size:23px">Bee-yond!</div>
  <p class="intro" style="left:35px;top:272px;width:310px;font-size:11px;line-height:1.45">Let the bees lead the way! Discover breathtaking destinations with <b>Mirvo Kalt</b>, your passport to unforgettable journeys.</p>

  <div class="bee" role="img" aria-label="Large bee in flight with a looping dashed trail" style="left:666px;top:2px;width:68px;height:94px"></div>

  <svg class="hex" style="left:503px;top:30px" width="174" height="151" viewBox="0 0 200 174">
    <polygon points="50,2 150,2 198,87 150,172 50,172 2,87" fill="var(--honey)"/>
    <polygon role="img" aria-label="Photo of Niagara Falls" points="58,12 142,12 186,87 142,162 58,162 14,87" fill="url(#photo-falls)"/>
    <polygon points="33,118 167,118 144,158 56,158" fill="var(--navy-band)" opacity=".9"/>
    <text class="hex-label" x="100" y="136" text-anchor="middle" font-size="15">NIAGARA</text>
    <text class="hex-label" x="100" y="153" text-anchor="middle" font-size="15">FALLS</text>
  </svg>
  <svg class="hex" style="left:347px;top:118px" width="174" height="151" viewBox="0 0 200 174">
    <polygon points="50,2 150,2 198,87 150,172 50,172 2,87" fill="var(--honey)"/>
    <polygon role="img" aria-label="Photo of a historic Ontario castle" points="58,12 142,12 186,87 142,162 58,162 14,87" fill="url(#photo-castle)"/>
    <polygon points="33,118 167,118 144,158 56,158" fill="var(--navy-band)" opacity=".9"/>
    <text class="hex-label" x="100" y="136" text-anchor="middle" font-size="15">ONTARIO</text>
    <text class="hex-label" x="100" y="153" text-anchor="middle" font-size="15">SITES</text>
  </svg>
  <svg class="hex" style="left:505px;top:203px" width="174" height="151" viewBox="0 0 200 174">
    <polygon points="50,2 150,2 198,87 150,172 50,172 2,87" fill="var(--honey)"/>
    <polygon role="img" aria-label="Photo of a great ancient wall over hills" points="58,12 142,12 186,87 142,162 58,162 14,87" fill="url(#photo-wall)"/>
    <polygon points="33,118 167,118 144,158 56,158" fill="var(--navy-band)" opacity=".9"/>
    <text class="hex-label" x="100" y="136" text-anchor="middle" font-size="15">GLOBAL</text>
    <text class="hex-label" x="100" y="153" text-anchor="middle" font-size="15">LANDMARKS</text>
  </svg>
  <svg class="dots" style="left:706px;top:316px" width="24" height="60"><rect width="24" height="60" fill="url(#dot-grid)"/></svg>

  <div class="footer" style="height:50px;width:560px;padding-left:37px;gap:26px;background:var(--navy)">
    <div class="footer__phone" style="gap:6px;font-size:19px">
      <span class="icon-phone" style="width:21px;height:21px"><svg width="11" height="11" viewBox="0 0 24 24"><path d="M6.6 10.8a15 15 0 0 0 6.6 6.6l2.2-2.2c.3-.3.7-.4 1-.2 1.1.4 2.3.6 3.6.6.6 0 1 .4 1 1V20c0 .6-.4 1-1 1A17 17 0 0 1 3 4c0-.6.4-1 1-1h3.5c.6 0 1 .4 1 1 0 1.3.2 2.5.6 3.6.1.3 0 .7-.2 1z" fill="var(--navy)"/></svg></span>0147 258 369</div>
    <div class="footer__contact" style="font-size:12.5px">
      <svg width="12" height="10" viewBox="0 0 22 16"><rect x="1" y="1" width="20" height="14" fill="none" stroke="#fff" stroke-width="2"/><path d="M1 1l10 8 10-8" fill="none" stroke="#fff" stroke-width="2"/></svg>
      info@mirvokalt.com &nbsp;|&nbsp; www.Mirvokalt.com</div>
  </div>
</section>

</body>
</html>
```